Crestline Lending Group Business Cards

We are looking to revamp the current business cards each of our locations uses. We are a lending company that specializes in personal loans, title loans, and tax services. We have locations in New Mexico, Texas, and Oklahoma.

We would like a cleaner, sleeker look while still highlighting what we offer. Title Loans, Personal Loans & Tax Services. We also want to include our referral fee somewhere on the card. We would like to see an English option as well as a Spanish option for the cards.

PLEASE NOTE: Some business cards do not include the employee's name but just the store's location, while others will include both.

These are double-sided business cards, and we would like to see proof if possible. I have included proofs of our current business cards for you to review below, as well as our company logo. Feel free to get creative with the logo, etc! Colors should match the logo; however, you do not need to use all of our logo colors if you don't want to.

```html
<!DOCTYPE html>
<html lang="en">
<head>
<meta charset="utf-8">
<title>Crestline Lending Group Business Cards</title>
<link rel="stylesheet" href="https://fonts.googleapis.com/css2?family=Poppins:wght@400;500;600&family=Cormorant+Garamond:wght@500&display=swap">
<style>
  :root {
    --sky: #27b1fd;
    --sky-deep: #1391d6;
    --navy: #0f2f3d;
    --ink: #12323f;
    --paper: #ffffff;
    --silver: #d9d9d9;
    --backdrop: #f4f6f8;
  }
  * { margin: 0; padding: 0; box-sizing: border-box; }
  html, body { width: 1200px; height: 1200px; overflow: hidden; }
  body {
    background: var(--backdrop);
    font-family: "Poppins", sans-serif;
    position: relative;
  }
  .card {
    position: absolute;
    left: 246px;
    width: 708px;
    height: 425px;
    overflow: hidden;
    background: linear-gradient(90deg, var(--silver) 0%, var(--paper) 30%, var(--paper) 62%, var(--silver) 100%);
  }
  .card--front { top: 143px; }
  .card--back { top: 632px; }
  .card__art { position: absolute; inset: 0; width: 100%; height: 100%; }

  .person { position: absolute; left: 72px; top: 54px; color: var(--ink); }
  .person__name { font-size: 40px; font-weight: 600; letter-spacing: -0.5px; line-height: 1; }
  .person__title { font-size: 15px; font-weight: 500; margin-top: 4px; }
  .person__rule { width: 68px; height: 2px; background: var(--sky); margin-top: 3px; }

  .contacts { position: absolute; left: 72px; top: 192px; list-style: none; color: var(--paper); }
  .contacts li { display: flex; align-items: flex-start; gap: 12px; font-size: 14px; line-height: 1.2; margin-bottom: 10px; }
  .contacts__icon {
    width: 23px; height: 23px; background: var(--paper); border-radius: 2px;
    display: flex; align-items: center; justify-content: center; flex: none;
  }
  .contacts__icon svg { width: 14px; height: 14px; }
  .contacts__text { padding-top: 3px; }

  .services { position: absolute; left: 72px; top: 352px; color: var(--paper); font-size: 17px; font-weight: 600; }

  .brand { position: absolute; text-align: center; color: var(--sky); }
  .brand__name { font-family: "Cormorant Garamond", serif; font-weight: 500; line-height: 0.95; }
  .brand__url { font-family: "Poppins", sans-serif; color: var(--ink); margin-top: 8px; white-space: nowrap; }
  .brand--front { left: 380px; top: 110px; width: 300px; }
  .brand--front .brand__name { font-size: 44px; }
  .brand--front .brand__url { font-size: 16px; }
  .brand--back { left: 94px; top: 118px; width: 520px; }
  .brand--back .brand__name { font-size: 46px; white-space: nowrap; }
  .brand--back .brand__url { font-size: 18px; margin-top: 10px; }
</style>
</head>
<body>

<section class="card card--front" aria-label="Card front">
  <svg class="card__art" viewBox="0 0 708 425" preserveAspectRatio="none">
    <defs>
      <radialGradient id="frontTexture" cx="0.85" cy="0.75" r="0.6">
        <stop offset="0" stop-color="#8ccbef" stop-opacity="0.55"/>
        <stop offset="1" stop-color="#8ccbef" stop-opacity="0"/>
      </radialGradient>
      <linearGradient id="frontBlue" x1="0" y1="0" x2="0" y2="1">
        <stop offset="0.6" stop-color="#27b1fd"/>
        <stop offset="1" stop-color="#1391d6"/>
      </linearGradient>
    </defs>
    <rect x="440" y="160" width="268" height="265" fill="url(#frontTexture)" role="img" aria-label="Soft halftone dot texture"/>
    <path d="M0,130 C150,135 330,180 460,290 C520,340 560,390 589,425 L0,425 Z" fill="url(#frontBlue)"/>
    <path d="M126,146 C260,172 385,232 476,302 C534,348 574,392 607,425 L589,425 C560,390 520,340 460,290 C360,205 250,160 126,146 Z" fill="var(--navy)"/>
  </svg>

  <div class="person">
    <p class="person__name">Maria Torres</p>
    <p class="person__title">Branch Manager</p>
    <div class="person__rule"></div>
  </div>

  <ul class="contacts">
    <li>
      <span class="contacts__icon"><svg viewBox="0 0 24 24"><path fill="#27b1fd" d="M6.6 10.8a15 15 0 0 0 6.6 6.6l2.2-2.2c.3-.3.7-.4 1-.2 1.1.4 2.3.6 3.6.6.6 0 1 .4 1 1V20c0 .6-.4 1-1 1A17 17 0 0 1 3 4c0-.6.4-1 1-1h3.5c.6 0 1 .4 1 1 0 1.3.2 2.5.6 3.6.1.3 0 .7-.2 1z"/></svg></span>
      <span class="contacts__text">(505) 555-0148</span>
    </li>
    <li>
      <span class="contacts__icon"><svg viewBox="0 0 24 24"><rect x="3" y="6" width="18" height="12" fill="none" stroke="#27b1fd" stroke-width="2"/><path d="M3 6l9 7 9-7" fill="none" stroke="#27b1fd" stroke-width="2"/></svg></span>
      <span class="contacts__text">hello@crestlinelending.com</span>
    </li>
    <li>
      <span class="contacts__icon"><svg viewBox="0 0 24 24"><circle cx="12" cy="12" r="9" fill="none" stroke="#27b1fd" stroke-width="2"/><path d="M3 12h18M12 3c3 3 3 15 0 18M12 3c-3 3-3 15 0 18" fill="none" stroke="#27b1fd" stroke-width="1.6"/></svg></span>
      <span class="contacts__text">www.crestlinelending.com</span>
    </li>
    <li>
      <span class="contacts__icon"><svg viewBox="0 0 24 24"><path fill="#27b1fd" d="M12 2a7 7 0 0 0-7 7c0 5 7 13 7 13s7-8 7-13a7 7 0 0 0-7-7zm0 9.5A2.5 2.5 0 1 1 12 6.5a2.5 2.5 0 0 1 0 5z"/></svg></span>
      <span class="contacts__text">48 Mesa Road, Suite B Anytown,<br>Texas 55555</span>
    </li>
  </ul>

  <p class="services">Title Loans • Personal Loans • Tax Services</p>

  <div class="brand brand--front">
    <p class="brand__name">Crestline Lending Group</p>
    <p class="brand__url">www.crestlinelending.com</p>
  </div>
</section>

<section class="card card--back" aria-label="Card back">
  <svg class="card__art" viewBox="0 0 708 425" preserveAspectRatio="none">
    <defs>
      <linearGradient id="backBlue" x1="0" y1="0" x2="1" y2="0">
        <stop offset="0.35" stop-color="#27b1fd"/>
        <stop offset="1" stop-color="#0f86c9"/>
      </linearGradient>
    </defs>
    <path d="M0,305 C80,325 150,335 190,333 C330,330 430,250 560,232 C620,224 670,222 708,222 L708,425 L0,425 Z" fill="url(#backBlue)" role="img" aria-label="Blue wave with soft halftone dot texture"/>
    <path d="M190,333 C330,320 430,240 560,214 C620,204 670,199 708,198 L708,222 C670,222 620,224 560,232 C430,250 330,330 190,333 Z" fill="var(--navy)"/>
  </svg>

  <div class="brand brand--back">
    <p class="brand__name">Crestline Lending Group</p>
    <p class="brand__url">www.crestlinelending.com</p>
  </div>
</section>

</body>
</html>
```